Falcrest security business card

Looking for a business card for my security company

Target Market(s)

Security

Industry/Entity Type

Security

Contact Information for Business Card

Name - Gil Marston. Title - General manager - direct 314 862.4490 website www. falcrestsecurityservices.example email - gil@ falcrestsecurityservices.example

Requirements
Must have
• Logo attached

```html
<!DOCTYPE html>
<html lang="en">
<head>
<meta charset="utf-8">
<title>Falcrest Security Services – Gil Marston</title>
<link rel="stylesheet" href="https://fonts.googleapis.com/css2?family=Montserrat:wght@300;400;500;800&display=swap">
<style>
  :root {
    --ink: #0c0b0a;
    --ink-soft: #1a1816;
    --gold: #c9a25c;
    --gold-deep: #8d6a32;
    --cream: #f4e7d0;
    --ghost: rgba(255, 255, 255, 0.05);
  }
  * { margin: 0; padding: 0; box-sizing: border-box; }
  html, body { width: 1200px; height: 686px; overflow: hidden; background: var(--ink); }
  .card {
    position: relative;
    width: 1200px;
    height: 686px;
    overflow: hidden;
    background: var(--ink);
    font-family: "Montserrat", sans-serif;
    color: var(--cream);
  }
  .texture {
    position: absolute;
    inset: 0;
    background:
      radial-gradient(ellipse 380px 700px at 820px 300px, rgba(60, 55, 50, 0.55), transparent 70%),
      radial-gradient(ellipse 300px 600px at 1120px 420px, rgba(45, 40, 36, 0.5), transparent 70%),
      linear-gradient(100deg, var(--ink) 0%, var(--ink-soft) 55%, var(--ink) 100%);
  }
  .streaks { position: absolute; inset: 0; }
  .ghost-name {
    position: absolute;
    left: -20px;
    top: 175px;
    font-size: 150px;
    font-weight: 800;
    letter-spacing: 4px;
    color: var(--ghost);
    white-space: nowrap;
  }
  .ghost-square {
    position: absolute;
    left: 170px;
    top: 50px;
    width: 290px;
    height: 130px;
    border: 10px solid var(--ghost);
  }
  .monogram {
    position: absolute;
    left: 683px;
    top: 59px;
    width: 137px;
    height: 137px;
    border: 3px solid var(--gold);
    display: flex;
    align-items: center;
    justify-content: center;
    font-size: 52px;
    font-weight: 500;
    color: var(--gold);
    letter-spacing: 2px;
  }
  .collab-mark {
    position: absolute;
    left: 860px;
    top: 108px;
    font-size: 28px;
    font-weight: 300;
    color: var(--cream);
  }
  .brand {
    position: absolute;
    left: 900px;
    top: 98px;
    font-size: 48px;
    font-weight: 800;
    letter-spacing: 1px;
    color: var(--gold);
  }
  .person {
    position: absolute;
    left: 97px;
    top: 380px;
    width: 548px;
    text-align: right;
  }
  .person-name {
    font-size: 60px;
    line-height: 1;
    text-align: left;
    white-space: nowrap;
    color: var(--cream);
    text-shadow: 0 3px 6px rgba(0,0,0,0.6);
  }
  .person-name .first { font-weight: 300; }
  .person-name .last { font-weight: 800; }
  .person-title {
    margin-top: 8px;
    font-size: 22px;
    font-weight: 400;
    letter-spacing: 0.5px;
  }
  .address {
    position: absolute;
    left: 140px;
    top: 550px;
    display: flex;
    gap: 14px;
    align-items: flex-start;
  }
  .address-text {
    font-size: 18px;
    line-height: 26px;
    font-weight: 400;
    text-transform: uppercase;
  }
  .address-text strong { font-weight: 800; }
  .contacts {
    position: absolute;
    left: 742px;
    top: 360px;
    list-style: none;
  }
  .contact {
    display: flex;
    align-items: center;
    gap: 24px;
  }
  .contact + .contact { margin-top: 22px; }
  .contact-icon { width: 36px; flex: none; display: flex; justify-content: center; }
  .contact-phone { font-size: 32px; font-weight: 400; letter-spacing: 0.5px; }
  .contact-text { font-size: 18px; line-height: 23px; font-weight: 400; text-transform: uppercase; }
</style>
</head>
<body>
<main class="card">
  <div class="texture" role="img" aria-label="Dark black brushstroke texture with fine gold streaks"></div>
  <svg class="streaks" width="1200" height="686" viewBox="0 0 1200 686" aria-hidden="true">
    <path d="M640 0 C 700 180, 690 420, 760 686" fill="none" stroke="#d8d2c6" stroke-width="2.5" opacity="0.8"/>
    <path d="M1025 0 C 1030 200, 1040 420, 1170 686" fill="none" stroke="var(--gold)" stroke-width="1.5" opacity="0.6"/>
    <path d="M140 0 C 150 30, 160 40, 175 60" fill="none" stroke="var(--gold)" stroke-width="1.5" opacity="0.5"/>
  </svg>

  <div class="ghost-square" aria-hidden="true"></div>
  <div class="ghost-name" aria-hidden="true">FALCREST</div>

  <div class="monogram">GM</div>
  <div class="collab-mark">X</div>
  <div class="brand">FALCREST</div>

  <section class="person">
    <h1 class="person-name"><span class="first">GIL</span> <span class="last">MARSTON</span></h1>
    <p class="person-title">GENERAL MANAGER</p>
  </section>

  <address class="address" style="font-style:normal">
    <svg width="34" height="42" viewBox="0 0 34 42" aria-hidden="true">
      <path d="M17 2 C8 2 2 9 2 17 C2 28 17 40 17 40 C17 40 32 28 32 17 C32 9 26 2 17 2 Z" fill="none" stroke="var(--gold)" stroke-width="3"/>
      <circle cx="17" cy="17" r="5.5" fill="var(--gold)"/>
    </svg>
    <p class="address-text">4410 Harborview Lane, <strong>Houston,</strong><br><strong>Texas, United States.</strong></p>
  </address>

  <ul class="contacts">
    <li class="contact">
      <span class="contact-icon">
        <svg width="30" height="30" viewBox="0 0 24 24" aria-hidden="true">
          <path d="M6.6 10.8c1.4 2.8 3.8 5.1 6.6 6.6l2.2-2.2c.3-.3.7-.4 1-.2 1.1.4 2.3.6 3.6.6.6 0 1 .4 1 1V20c0 .6-.4 1-1 1C10.6 21 3 13.4 3 4c0-.6.4-1 1-1h3.5c.6 0 1 .4 1 1 0 1.3.2 2.5.6 3.6.1.3 0 .7-.2 1z" fill="var(--gold)"/>
        </svg>
      </span>
      <span class="contact-phone">314 862.4490</span>
    </li>
    <li class="contact">
      <span class="contact-icon">
        <svg width="30" height="22" viewBox="0 0 30 22" aria-hidden="true">
          <rect x="1.5" y="1.5" width="27" height="19" fill="none" stroke="var(--gold)" stroke-width="2.5"/>
          <path d="M2 2 L15 12 L28 2" fill="none" stroke="var(--gold)" stroke-width="2.5"/>
        </svg>
      </span>
      <span class="contact-text">GIL@FALCRESTSECURITY<br>SERVICES.EXAMPLE</span>
    </li>
    <li class="contact">
      <span class="contact-icon">
        <svg width="34" height="34" viewBox="0 0 34 34" aria-hidden="true">
          <g fill="none" stroke="var(--gold)" stroke-width="2">
            <circle cx="17" cy="17" r="15"/>
            <ellipse cx="17" cy="17" rx="7" ry="15"/>
            <line x1="2" y1="17" x2="32" y2="17"/>
            <path d="M5 9 H29 M5 25 H29"/>
          </g>
        </svg>
      </span>
      <span class="contact-text">FALCRESTSECURITY<br>SERVICES.EXAMPLE</span>
    </li>
  </ul>
</main>
</body>
</html>
```